Healthcare Service Provider looking for PowerPoint Template

ROV Profile of the company & business activity
===================================
ROV is the leading after-sale healthcare services provider in Kuwait. The IT department in the company sells & executes Healthcare IT projects in hospitals that mainly cover:

1. IT Infrastructure covering data center, disaster recovery, servers, virtualization, backup, redundancy & high-availability, multi-site connectivity, wired & wireless networking, OS & network management, software subscriptions, …etc.

2. Healthcare IT systems covering the Hospital Management system, Electronic Medical Record, evidence-based clinical content, clinical decision support systems, Radiology information system, Lab information system, pharmacy management system, ICU system, dental system, dietary & nutrition system, integration with 3rd party systems in the hospital

3. Human resources covering the company specialized teams of clinical informatics specialists, pharmacists, nurses, project managers, user experience specialists, integration specialists, systems analysts, systems developers, DB administrators, Network administrators, system architects, systems engineers, …

The assortment of these professionals handle the services for implementing specialty Healthcare IT systems, training hospital staff & healthcare professionals, on-site support & maintenance of implemented healthcare systems at the hospital

Requested design job
================
We require a PowerPoint template to be used by the IT department in presenting sales & marketing pitches, commercial proposals, projects, and related to the business activities described in the profile.

The design of the PowerPoint template should:

. be personalized for the business activities of the IT department. promote the corporate brand identity of the company. provide clean, modern and fluent look & feel for presenting on screen, projector or printing. include font selection & design as part of the template design. light colored background

. multiple page layouts & slide types like a cover slide, title slide, different types of content slides, ….

. include design collaterals like icons and clip-arts

. have common design elements in PowerPoint Master slides

Included are the current corporate logos of the company.

In summary, simplicity, fluency and personality are key to the design we seek.

Requirements
Must have
• The design of the PowerPoint template should:
• . be personalized for the business activities of the IT department. promote the corporate brand identity of the company. provide clean, modern and fluent look & feel for presenting on screen, projector or printing. include font selection & design as part of the template design. light colored background
• . multiple page layouts & slide types like a cover slide, title slide, different types of content slides, ….
• . include design collaterals like icons and clip-arts
• . have common design elements in PowerPoint Master slides

```html
<!DOCTYPE html>
<html lang="en">
<head>
<meta charset="utf-8">
<title>ROV Presentation Template</title>
<link href="https://fonts.googleapis.com/css2?family=Open+Sans:wght@400;600;700&family=Noto+Kufi+Arabic:wght@400;600&display=swap" rel="stylesheet">
<style>
:root{
  --page:#e7e7f8;
  --navy:#14246b;
  --navy-dark:#0e1a52;
  --ink:#1b1b1b;
  --grey:#d9d9d9;
  --grey-light:#ececec;
  --white:#ffffff;
  --magenta:#c2185b;
  --purple:#3a0f4d;
}
*{box-sizing:border-box;margin:0;padding:0}
html,body{width:1200px;height:2498px;overflow:hidden}
body{background:var(--page);font-family:"Open Sans",Arial,sans-serif;color:var(--ink);position:relative}
.slide{position:absolute;left:120px;width:960px;background:var(--white);overflow:hidden}
.lorem{font-size:15px;line-height:1.35;text-align:center}

/* cover */
.cover{top:110px;height:730px}
.cover-photo{position:absolute;inset:0;background:radial-gradient(circle at 80% 20%,#ff4f8a 0,#c2185b 25%,#5a1460 60%,#25093a 100%)}
.cover-band{position:absolute;left:0;top:190px;width:960px;height:210px;background:var(--white);display:flex;align-items:center}
.brand-mark{width:300px;height:210px;background:var(--navy);display:flex;align-items:center;justify-content:center;gap:16px;color:var(--white);font-weight:700;font-size:64px}
.brand-mark .square{width:30px;height:30px;background:var(--white)}
.company{padding-left:30px;color:var(--navy)}
.company-en{font-size:38px;font-weight:400}
.company-en small{font-size:20px}
.company-ar{font-family:"Noto Kufi Arabic",sans-serif;font-size:40px;font-weight:600;direction:rtl;text-align:left}
.contact{position:absolute;left:30px;display:flex;align-items:center;gap:22px;color:var(--white);font-size:17px}
.contact svg{width:28px;height:28px}

/* text slide */
.text-slide{top:876px;height:364px}
.text-photo{position:absolute;left:0;top:0;width:400px;height:364px;background:linear-gradient(135deg,#8fa6d8,#2c4a9a 55%,#13245e)}
.text-body{position:absolute;left:420px;top:20px;width:520px}
.slide-title{font-size:26px;font-weight:400;text-align:center;color:#333;margin-bottom:10px}
.text-body .lorem{font-size:13px;line-height:1.22}
.mini-logo{position:absolute;right:14px;bottom:10px;font-weight:700;color:var(--navy);font-size:22px}

/* icon grid slide */
.grid-slide{top:1260px;height:555px}
.cell{position:absolute;display:flex;flex-direction:column;align-items:center;justify-content:center;gap:16px;padding:0 30px}
.cell svg{width:44px;height:44px;fill:var(--ink)}
.cell .lorem{font-size:15px}
.c1{left:0;top:0;width:320px;height:277px;background:var(--grey)}
.c2{left:0;top:277px;width:320px;height:278px;background:var(--grey-light)}
.c3{left:750px;top:0;width:210px;height:277px;background:var(--white);padding:0 14px}
.c4{left:750px;top:277px;width:210px;height:278px;background:var(--grey-light);padding:0 14px}
.city-photo{position:absolute;left:320px;top:0;width:430px;height:555px;background:linear-gradient(180deg,#c9d6e3 0,#9fb4c6 45%,#4d6275 75%,#2c3a48)}

/* cards slide */
.cards-slide{top:1843px;height:584px}
.rule{position:absolute;left:0;top:26px;width:960px;height:10px}
.rule .tab{position:absolute;left:0;top:-8px;width:22px;height:26px;background:var(--navy)}
.rule .line{position:absolute;left:40px;top:0;width:920px;height:8px;background:var(--navy)}
.cards-slide .slide-title{position:absolute;top:80px;width:100%}
.card{position:absolute;top:235px;width:240px;height:349px;padding:110px 24px 0}
.card .lorem{font-size:15px;line-height:1.3}
.card.light{background:var(--grey-light)}
.card.dark{background:var(--navy);color:var(--white)}
.card.white{background:var(--white)}
.badge{position:absolute;top:165px;width:110px;height:110px;border-radius:50%;background:var(--white);border:3px solid var(--navy);display:flex;align-items:center;justify-content:center;color:var(--navy);font-weight:700;font-size:28px}
</style>
</head>
<body>

<section class="slide cover">
  <div class="cover-photo" role="img" aria-label="Close-up photo of glowing red LED lights on a dark purple panel"></div>
  <div class="cover-band">
    <div class="brand-mark"><span class="square"></span><span>ROV</span></div>
    <div class="company">
      <div class="company-en">ROV Systems Company <small>K.S.C.P</small></div>
      <div class="company-ar">شركة روف للأنظمة ش.م.ك.ع</div>
    </div>
  </div>
  <div class="contact" style="top:508px">
    <svg viewBox="0 0 24 24"><circle cx="12" cy="12" r="12" fill="#000"/><path d="M8.5 6.5l2 2-1.2 1.6a7 7 0 0 0 4.6 4.6l1.6-1.2 2 2-1.5 2c-4.8-.3-8.8-4.3-9.1-9.1z" fill="#fff"/></svg>
    <span>Phone Number</span>
  </div>
  <div class="contact" style="top:576px">
    <svg viewBox="0 0 24 24"><circle cx="12" cy="12" r="12" fill="#000"/><circle cx="12" cy="12" r="6" fill="none" stroke="#fff" stroke-width="1.4"/><path d="M6 12h12M12 6c-2.5 3-2.5 9 0 12M12 6c2.5 3 2.5 9 0 12" fill="none" stroke="#fff" stroke-width="1.2"/></svg>
    <span>www.website.com</span>
  </div>
</section>

<section class="slide text-slide">
  <div class="text-photo" role="img" aria-label="Photo of blue glass office towers seen from below"></div>
  <div class="text-body">
    <h2 class="slide-title">SLIDE TITLE</h2>
    <p class="lorem">"Lorem ipsum dolor sit amet, consectetur adipiscing elit, sed do eiusmod tempor incididunt ut labore et dolore magna aliqua. Ut enim ad minim veniam, quis nostrud exercitation ullamco laboris nisi ut aliquip ex ea commodo consequat. Duis aute irure dolor in reprehenderit in voluptate velit esse cillum dolore eu fugiat nulla pariatur. Excepteur sint occaecat cupidatat non proident, sunt in culpa qui officia deserunt mollit anim id est laborum." "Lorem ipsum dolor sit amet, consectetur adipiscing elit, sed do eiusmod tempor incididunt ut labore et dolore magna aliqua. Ut enim ad minim veniam, quis nostrud exercitation ullamco laboris nisi ut aliquip ex ea commodo consequat. Duis aute irure dolor in reprehenderit in voluptate velit esse cillum dolore eu fugiat nulla pariatur. Excepteur sint occaecat cupidatat non proident, sunt in culpa qui officia deserunt mollit anim id est laborum."</p>
  </div>
  <div class="mini-logo">ROV</div>
</section>

<section class="slide grid-slide">
  <div class="cell c1">
    <svg viewBox="0 0 24 24"><rect x="3" y="4" width="4" height="16"/><rect x="8" y="4" width="4" height="16"/><rect x="13" y="5" width="4" height="15" transform="rotate(-12 15 12)"/></svg>
    <p class="lorem">"Lorem ipsum dolor sit amet, consectetur adipiscing elit, sed do eiusmod tempor incididunt ut labore et dolore magna aliqua. Ut enim ad minim veniam</p>
  </div>
  <div class="cell c2">
    <svg viewBox="0 0 24 24"><rect x="3" y="4" width="18" height="11"/><path d="M11 15h2v3l4 3h-2l-3-2-3 2H7l4-3z"/><path d="M2 3h20v1.5H2z"/></svg>
    <p class="lorem">"Lorem ipsum dolor sit amet, consectetur adipiscing elit, sed do eiusmod tempor incididunt ut labore et dolore magna aliqua. Ut enim ad minim veniam</p>
  </div>
  <div class="city-photo" role="img" aria-label="Photo of a city skyline with a tall communications tower"></div>
  <div class="cell c3">
    <svg viewBox="0 0 24 24"><path d="M2 9a14 14 0 0 1 20 0l-1.5 1.5a12 12 0 0 0-17 0z"/><path d="M5.5 12.5a9 9 0 0 1 13 0L17 14a7 7 0 0 0-10 0z"/><path d="M9 16a4 4 0 0 1 6 0l-3 3z"/></svg>
    <p class="lorem">"Lorem ipsum dolor sit amet, consectetur adipiscing elit, sed do eiusmod tempor incididunt ut labore et dolore magna aliqua. Ut enim ad minim veniam</p>
  </div>
  <div class="cell c4">
    <svg viewBox="0 0 24 24"><rect x="3" y="15" width="3" height="6"/><rect x="8" y="12" width="3" height="9"/><rect x="13" y="9" width="3" height="12"/><rect x="18" y="5" width="3" height="16"/></svg>
    <p class="lorem">"Lorem ipsum dolor sit amet, consectetur adipiscing elit, sed do eiusmod tempor incididunt ut labore et dolore magna aliqua. Ut enim ad minim veniam</p>
  </div>
</section>

<section class="slide cards-slide">
  <div class="rule"><span class="tab"></span><span class="line"></span></div>
  <h2 class="slide-title">SLIDE TITLE</h2>
  <div class="card light" style="left:0"><p class="lorem">"Lorem ipsum dolor sit amet, consectetur adipiscing elit, sed do eiusmod tempor incididunt ut labore et dolore magna aliqua. Ut enim ad minim veniam, quis nostrud exercitation ullamco laboris nisi ut</p></div>
  <div class="card dark" style="left:240px"><p class="lorem">"Lorem ipsum dolor sit amet, consectetur adipiscing elit, sed do eiusmod tempor incididunt ut labore et dolore magna aliqua. Ut enim ad minim veniam, quis nostrud exercitation ullamco laboris nisi ut</p></div>
  <div class="card white" style="left:480px"><p class="lorem">"Lorem ipsum dolor sit amet, consectetur adipiscing elit, sed do eiusmod tempor incididunt ut labore et dolore magna aliqua. Ut enim ad minim veniam, quis nostrud exercitation ullamco laboris nisi ut</p></div>
  <div class="card dark" style="left:720px"><p class="lorem">"Lorem ipsum dolor sit amet, consectetur adipiscing elit, sed do eiusmod tempor incididunt ut labore et dolore magna aliqua. Ut enim ad minim veniam, quis nostrud exercitation ullamco laboris nisi ut</p></div>
  <div class="badge" style="left:65px">ROV</div>
  <div class="badge" style="left:305px">ROV</div>
  <div class="badge" style="left:545px">ROV</div>
  <div class="badge" style="left:785px">ROV</div>
</section>

</body>
</html>
```